Business card for our large format printing and installation business

We want a professional looking business card for our business. We manufacture and install Signs.

On the back of the card add this info
Large Format Graphics Printing & Installations, Event Graphics, Banners, Posters, Vehicle Fleet Graphics, Boat Wraps, Wall Murals, Decals,Displays,Signs,Plaques,Digital Signs

On the Front of the card add the Tallowfern Signs logo, plus On the back of the card add the Orange Tallowfern Wraps logo. The 2 vector logos are attached to the design brief.

Target Market(s)

Local business owners

Contact Information for Business Card

Colors
f37122
f68d4e
f9ba93

Requirements
Must have
• On the Front of the card add the Tallowfern Signs logo, plus On the back of the card add the Orange Tallowfern Wraps logo. The 2 vector logos are attached to the design brief.

```html
<!DOCTYPE html>
<html lang="en">
<head>
<meta charset="utf-8">
<title>Tallowfern Signs – Business Card</title>
<link rel="stylesheet" href="https://fonts.googleapis.com/css2?family=Montserrat:wght@400;500;800&family=Tinos:wght@700&display=swap">
<style>
  :root {
    --stage: #2b2e33;
    --card: #111111;
    --logo: #f7a51e;
    --wraps: #f37122;
    --accent-start: #f37122;
    --accent-end: #f7d70a;
    --title: #f9c316;
    --ink: #f2f2f2;
    --muted: #f9ba93;
    --icon: #f5b71a;
  }
  * { margin: 0; padding: 0; box-sizing: border-box; }
  html, body { width: 1200px; height: 1000px; overflow: hidden; }
  body {
    background: var(--stage);
    position: relative;
    font-family: "Montserrat", sans-serif;
    color: var(--ink);
  }
  .card {
    position: absolute;
    left: 250px;
    width: 700px;
    height: 400px;
    background: var(--card);
    box-shadow: 0 10px 30px rgba(0,0,0,.45);
  }
  .card--back { top: 60px; }
  .card--front { top: 530px; }

  .brand-name {
    font-family: "Montserrat", sans-serif;
    font-weight: 800;
    color: var(--logo);
    line-height: 1;
    letter-spacing: .5px;
  }

  /* Back */
  .card--back .brand-name {
    position: absolute;
    left: 0; right: 0; top: 95px;
    text-align: center;
    font-size: 60px;
  }
  .services {
    position: absolute;
    left: 70px; right: 70px; top: 205px;
    text-align: center;
    font-size: 13px;
    line-height: 1.7;
    color: var(--ink);
  }
  .services-lead {
    font-weight: 500;
    color: var(--muted);
    margin-bottom: 2px;
  }
  .wraps-name {
    position: absolute;
    left: 0; right: 0; top: 318px;
    text-align: center;
    font-family: "Montserrat", sans-serif;
    font-weight: 800;
    font-size: 26px;
    line-height: 1;
    color: var(--wraps);
  }

  /* Front */
  .card--front .brand-name {
    position: absolute;
    left: 55px; top: 55px;
    font-size: 34px;
  }
  .divider {
    position: absolute;
    left: 40px; top: 195px;
    width: 520px; height: 2px;
    background: linear-gradient(90deg, var(--accent-start), var(--accent-end));
  }
  .holder {
    position: absolute;
    right: 45px; top: 152px;
    text-align: right;
  }
  .holder-name {
    font-family: "Tinos", serif;
    font-weight: 700;
    font-size: 30px;
    line-height: 1;
    letter-spacing: 1px;
    color: #ffffff;
  }
  .holder-title {
    margin-top: 18px;
    font-size: 15px;
    line-height: 1;
    color: var(--title);
  }
  .contact {
    position: absolute;
    left: 45px; top: 215px;
    font-size: 14px;
    line-height: 1.35;
  }
  .contact-address { margin-bottom: 8px; padding-left: 4px; }
  .contact-list { list-style: none; }
  .contact-list li {
    display: flex;
    align-items: center;
    gap: 8px;
    height: 20px;
  }
  .contact-list svg { width: 12px; height: 12px; flex: none; fill: var(--icon); }
</style>
</head>
<body>

<section class="card card--back" aria-label="Card back">
  <div class="brand-name">Tallowfern Signs</div>
  <div class="services">
    <p class="services-lead">Large Format Graphics Printing &amp; Installations</p>
    <p>Event Graphics · Banners · Posters · Vehicle Fleet Graphics · Boat Wraps<br>
       Wall Murals · Decals · Displays · Signs · Plaques · Digital Signs</p>
  </div>
  <div class="wraps-name">Tallowfern Wraps</div>
</section>

<section class="card card--front" aria-label="Card front">
  <div class="brand-name">Tallowfern Signs</div>

  <div class="divider"></div>

  <div class="holder">
    <div class="holder-name">Marcus Hale</div>
    <div class="holder-title">Owner</div>
  </div>

  <div class="contact">
    <p class="contact-address">418 Ridgeline Rd. Cedar Falls,<br>AR 72999</p>
    <ul class="contact-list">
      <li>
        <svg viewBox="0 0 24 24" aria-hidden="true"><path d="M6.6 10.8a15.1 15.1 0 0 0 6.6 6.6l2.2-2.2a1 1 0 0 1 1-.25 11.4 11.4 0 0 0 3.6.57 1 1 0 0 1 1 1V20a1 1 0 0 1-1 1A17 17 0 0 1 3 4a1 1 0 0 1 1-1h3.5a1 1 0 0 1 1 1c0 1.25.2 2.45.57 3.6a1 1 0 0 1-.25 1z"/></svg>
        <span>555-014-2290</span>
      </li>
      <li>
        <svg viewBox="0 0 24 24" aria-hidden="true"><path d="M7 1h10a2 2 0 0 1 2 2v18a2 2 0 0 1-2 2H7a2 2 0 0 1-2-2V3a2 2 0 0 1 2-2zm0 3v14h10V4zm5 15.5a1 1 0 1 0 0 2 1 1 0 0 0 0-2z"/></svg>
        <span>555-018-7731</span>
      </li>
      <li>
        <svg viewBox="0 0 24 24" aria-hidden="true"><path d="M2 5h20v14H2zm2 2v.4l8 5 8-5V7zm0 2.8V17h16V9.8l-8 5z"/></svg>
        <span>info@TallowfernSigns.com</span>
      </li>
      <li>
        <svg viewBox="0 0 24 24" aria-hidden="true"><path d="M12 2a10 10 0 1 0 0 20 10 10 0 0 0 0-20zm6.9 6h-3a15.6 15.6 0 0 0-1.4-3.6A8 8 0 0 1 18.9 8zM12 4a14 14 0 0 1 1.9 4h-3.8A14 14 0 0 1 12 4zM4.3 14a8.2 8.2 0 0 1 0-4h3.4a16.5 16.5 0 0 0 0 4zm.8 2h3a15.6 15.6 0 0 0 1.4 3.6A8 8 0 0 1 5.1 16zm3-8h-3a8 8 0 0 1 4.4-3.6A15.6 15.6 0 0 0 8.1 8zM12 20a14 14 0 0 1-1.9-4h3.8A14 14 0 0 1 12 20zm2.3-6H9.7a14.7 14.7 0 0 1 0-4h4.6a14.7 14.7 0 0 1 0 4zm.2 5.6a15.6 15.6 0 0 0 1.4-3.6h3a8 8 0 0 1-4.4 3.6zm1.8-5.6a16.5 16.5 0 0 0 0-4h3.4a8.2 8.2 0 0 1 0 4z"/></svg>
        <span>www.TallowfernSigns.com</span>
      </li>
    </ul>
  </div>
</section>

</body>
</html>
```